Greenhollow Remedies Alternative Medicine. Herbal Consulations+Wellness Therapies.

Just a quick background here. I established my massage business in 2006 and have mentored under a ND for several years as I finished my studies as an Herbalist. My main area is Kansas City, targeting all ages. I have decided to throw away all my old marketing material, business name and join 2015 in creating a bigger and better Herbal practice. What we specialize in is full body healing. Emotional healing as well as physical healing with herbs, while nurturing a healthy spiritual life. Mind, body and spirit is key, but herbs for healing are the center here. I would really like to go earthy and artistic with this. Something very unique and hip, that keeps the earthy vibe...so get your creative juices flowing. Attached are a few examples I have taken a liking to. I'd be okay seeing a few cards with some of these pictures on one side of the card or something new. If possible the final design should tie in the name of the busines so people understand where the spoon comes in. I got this idea from my Grandma's garden. When I was a child she would mark her herbs with spoons, similar to the picture attached.

Target Market(s)

Health Market, any age wanting to improve health

Industry/Entity Type

Marketing

Contact Information for Business Card

Greenhollow Remedies
Alternative Medicine
Clara Whitfield, LMT, CNHP, MH
27314 W County 12 Road
Linden Falls, WR 00418
555.246.0179
Holistic therapies for mind, body & spirit
Herbal Consultations + Wellness Therapies

Requirements
Must have
• I would like Alternative Medicine to pop as people are viewing the card
Nice to have
• I would like to have it double-sided. Picture on one side and description on the other. I like what I am seeing already with some of the cards
• Just a fun thought, I added another photo to the mix. It is a coffee chart. I thought, I'd like to see an herb chart similar to this on the back side of my card. If this is doable awesome, if not no biggie. It would be fun for people to look at the list of herbs with their name below.
Should not have
• I hope to distinguish between a business in holistic modalities vs. a food company, as the name can be confusing at first. But I'm trusting that in the end it will work fantastic!
• PLEASE MAKE NOT...File 6 photo is a sample business card of what I like and should NOT be used on my card. All other photos are fine. And, if you find any other photos that you think would go well, go for it. I'm open to possibilities. Thank you.

```html
<!DOCTYPE html>
<html lang="en">
<head>
<meta charset="utf-8">
<title>Greenhollow Remedies – Business Card</title>
<link href="https://fonts.googleapis.com/css2?family=Oxygen:wght@300;400;700&display=swap" rel="stylesheet">
<style>
  :root {
    --page-bg: #e9e7e2;
    --green-light: #3f8f40;
    --green-mid: #2c7230;
    --green-dark: #1d5520;
    --band-light: #fafafa;
    --band-dark: #dedede;
    --band-text: #3d9a3f;
    --ink-light: #ffffff;
    --rule: rgba(255, 255, 255, 0.75);
  }
  * { margin: 0; padding: 0; box-sizing: border-box; }
  html, body {
    width: 1200px;
    height: 818px;
    overflow: hidden;
    background: var(--page-bg);
    font-family: "Oxygen", sans-serif;
  }
  .card {
    position: absolute;
    left: 80px;
    top: 112px;
    width: 1040px;
    height: 594px;
    border-radius: 28px;
    overflow: hidden;
    background: radial-gradient(ellipse at 60% 55%, var(--green-light) 0%, var(--green-mid) 45%, var(--green-dark) 100%);
    color: var(--ink-light);
    box-shadow: 0 10px 30px rgba(0, 0, 0, 0.18);
  }
  .card__facets {
    position: absolute;
    inset: 0;
    background: linear-gradient(125deg, rgba(255,255,255,0.05) 0%, rgba(255,255,255,0) 40%, rgba(255,255,255,0.06) 70%, rgba(0,0,0,0.05) 100%);
  }
  .card__rule-v {
    position: absolute;
    top: 0;
    bottom: 96px;
    width: 1.5px;
    background: var(--rule);
  }
  .card__rule-v--left { left: 120px; }
  .card__rule-v--right { right: 120px; }
  .brand {
    position: absolute;
    top: 52px;
    left: 140px;
    right: 140px;
    text-align: center;
  }
  .brand__name {
    font-size: 72px;
    font-weight: 400;
    line-height: 1;
    white-space: nowrap;
  }
  .brand__tagline {
    margin-top: 14px;
    font-size: 30px;
    font-weight: 300;
    letter-spacing: 0.5em;
    padding-left: 0.5em;
  }
  .practitioner {
    position: absolute;
    top: 206px;
    left: 120px;
    right: 120px;
    text-align: center;
  }
  .practitioner__name {
    font-size: 36px;
    font-weight: 700;
    line-height: 1.1;
  }
  .practitioner__creds {
    display: flex;
    align-items: center;
    gap: 18px;
    margin-top: 4px;
    font-size: 19px;
    font-weight: 300;
  }
  .practitioner__creds::before,
  .practitioner__creds::after {
    content: "";
    flex: 1;
    height: 1.5px;
    background: var(--rule);
  }
  .practitioner__phone {
    margin-top: 14px;
    font-size: 44px;
    font-weight: 300;
    letter-spacing: 0.02em;
  }
  .services {
    position: absolute;
    top: 388px;
    left: 130px;
    right: 130px;
    text-align: center;
    font-size: 21px;
    font-weight: 700;
    line-height: 1.4;
  }
  .address-band {
    position: absolute;
    left: 0;
    right: 0;
    bottom: 0;
    height: 96px;
    background: linear-gradient(180deg, var(--band-light), var(--band-dark));
    display: flex;
    align-items: center;
    justify-content: center;
    color: var(--band-text);
    font-size: 29px;
    font-weight: 400;
  }
</style>
</head>
<body>
  <article class="card">
    <div class="card__facets"></div>
    <span class="card__rule-v card__rule-v--left"></span>
    <span class="card__rule-v card__rule-v--right"></span>

    <header class="brand">
      <h1 class="brand__name">Greenhollow Remedies</h1>
      <p class="brand__tagline">Alternative Medicine</p>
    </header>

    <section class="practitioner">
      <p class="practitioner__name">Clara Whitfield</p>
      <p class="practitioner__creds">LMT, CNHP</p>
      <p class="practitioner__phone">555.246.0179</p>
    </section>

    <p class="services">
      Holistic therapies for mind &amp; body Herbal Consultations Perception Reframing<br>
      stress management coaching Massage therapy
    </p>

    <footer class="address-band">
      MH 27314 W County 12 Road Linden Falls, WR 00418
    </footer>
  </article>
</body>
</html>
```